Creating a Label for the Wine "Sing by Candle"

As the name suggest, this wine is the one people must to take home. Sing by candle is the perfect wine to drink at home with you family and friends. Customers should be able to associate this label with happy moments spent with their loved ones. The dimensions can be between 9cm x 11,5 and 12cm x 8 cm.

```html
<!DOCTYPE html>
<html lang="en">
<head>
<meta charset="utf-8">
<title>Sing by Candle – Malbec Label</title>
<link rel="stylesheet" href="https://fonts.googleapis.com/css2?family=Cabin:wght@700&family=Marcellus&family=Cormorant+Garamond:wght@700&display=swap">
<style>
  :root {
    --backdrop: #2a2a2b;
    --backdrop-edge: #1f1f20;
    --label-light: #3d3d40;
    --label-dark: #1b1b1d;
    --ink-white: #f2f2f0;
    --accent-amber: #eaa11f;
  }
  * { box-sizing: border-box; margin: 0; padding: 0; }
  html, body {
    width: 1200px;
    height: 1095px;
    overflow: hidden;
  }
  body {
    background: radial-gradient(ellipse at 50% 45%, var(--backdrop) 0%, var(--backdrop-edge) 100%);
    position: relative;
  }
  .wine-label {
    position: absolute;
    left: 390px;
    top: 298px;
    width: 458px;
    height: 580px;
    background: linear-gradient(160deg, var(--label-light) 0%, #2a2a2d 45%, var(--label-dark) 100%);
    box-shadow: 0 2px 10px rgba(0, 0, 0, 0.35);
  }
  .wordmark {
    position: absolute;
    left: 0;
    right: 0;
    top: 104px;
    text-align: center;
    font-family: "Cabin", sans-serif;
    font-weight: 700;
    font-size: 118px;
    line-height: 92px;
    letter-spacing: -2px;
    color: var(--ink-white);
  }
  .wordmark span { display: block; }
  .varietal {
    position: absolute;
    left: 0;
    right: 0;
    top: 486px;
    text-align: center;
    font-family: "Marcellus", serif;
    font-size: 19px;
    letter-spacing: 4px;
    color: var(--ink-white);
  }
  .vintage {
    position: absolute;
    left: 0;
    right: 0;
    top: 508px;
    text-align: center;
    font-family: "Cormorant Garamond", serif;
    font-weight: 700;
    font-size: 20px;
    letter-spacing: 4px;
    color: var(--accent-amber);
  }
</style>
</head>
<body>
  <main class="wine-label">
    <h1 class="wordmark">
      <span>sing</span>
      <span>by</span>
      <span>candle</span>
    </h1>
    <p class="varietal">MALBEC</p>
    <p class="vintage">2014</p>
  </main>
</body>
</html>
```